New Business Card Design Project

Looking for a modern business card design for an import distribution business for industrial technical products. The winning design will translate modern, sophistication, technical, professional and sustainable.

Target Market(s)

Technical customers

Industry/Entity Type

Business

Contact Information for Business Card

Dean Harlow
Sales Manager
M: 0471 625 183
P: 1300 872 619
dean@volkarsystems.com.au
4/18 Galloway Crest Road
Harwood Vale NSW 2163
www.volkarsystems.com.au

Font styles to use
Sans Serif

Colors
ec1f27
606060
000000
fbfbfb

Requirements
Must have
• My Logo which is the Volkar Systems logo attached
Nice to have
• Eurostile Bold font

```html
<!DOCTYPE html>
<html lang="en">
<head>
<meta charset="utf-8">
<title>Volkar Systems – Business Card</title>
<link rel="stylesheet" href="https://fonts.googleapis.com/css2?family=Exo+2:wght@400;700&family=PT+Serif:wght@400&display=swap">
<style>
  :root {
    --red: #ec1f27;
    --slate: #5c6068;
    --grey: #606060;
    --ink: #000000;
    --paper: #fbfbfb;
    --backdrop: #2b2b2d;
  }
  html, body {
    margin: 0;
    width: 1200px;
    height: 997px;
    overflow: hidden;
    background: var(--backdrop);
  }
  .canvas {
    position: relative;
    width: 1200px;
    height: 997px;
  }
  .card {
    position: absolute;
    width: 520px;
    height: 317px;
    background: var(--paper);
    border-radius: 18px;
    overflow: hidden;
  }
  .card--front { left: 60px; top: 170px; }
  .card--back  { left: 620px; top: 500px; }
  .card__swoosh {
    position: absolute;
    inset: 0;
    width: 100%;
    height: 100%;
  }
  .brand {
    position: absolute;
    display: flex;
    align-items: center;
    gap: 10px;
    font-family: "Exo 2", sans-serif;
    font-weight: 700;
    color: var(--red);
    text-transform: uppercase;
    letter-spacing: 1px;
    white-space: nowrap;
  }
  .brand__square {
    display: block;
    background: var(--red);
  }
  .card--front .brand { right: 34px; top: 34px; font-size: 22px; }
  .card--front .brand__square { width: 20px; height: 20px; }
  .card--back .brand { left: 50%; top: 112px; transform: translateX(-50%); font-size: 38px; gap: 14px; }
  .card--back .brand__square { width: 34px; height: 34px; }

  .person {
    position: absolute;
    left: 30px;
    top: 128px;
    font-family: "PT Serif", serif;
  }
  .person__name {
    margin: 0;
    font-family: "Exo 2", sans-serif;
    font-size: 18px;
    color: var(--red);
  }
  .person__title {
    margin: 0;
    font-size: 12px;
    color: var(--grey);
  }
  .contact {
    position: absolute;
    left: 22px;
    bottom: 26px;
    margin: 0;
    padding: 0;
    list-style: none;
    font-family: "PT Serif", serif;
    font-size: 12.5px;
    line-height: 18px;
    color: var(--paper);
  }
  .contact__item {
    display: flex;
    align-items: center;
    gap: 10px;
  }
  .contact__icon {
    width: 11px;
    height: 11px;
    fill: #1e1f22;
  }
  .website {
    position: absolute;
    right: 28px;
    bottom: 18px;
    margin: 0;
    font-family: "Exo 2", sans-serif;
    font-size: 14px;
    letter-spacing: 0.5px;
    color: var(--paper);
  }
</style>
</head>
<body>
<main class="canvas">

  <section class="card card--front" aria-label="Business card, contact side">
    <svg class="card__swoosh" viewBox="0 0 520 317" preserveAspectRatio="none" aria-hidden="true">
      <path d="M0,222 C170,186 350,118 520,100 L520,317 L0,317 Z" fill="var(--slate)"/>
      <path d="M0,196 C170,156 340,98 500,86 C350,106 180,170 0,212 Z" fill="var(--red)"/>
    </svg>
    <div class="brand"><span class="brand__square"></span>Volkar Systems</div>
    <div class="person">
      <p class="person__name">Dean Harlow</p>
      <p class="person__title">Sales Manager</p>
    </div>
    <ul class="contact">
      <li class="contact__item">
        <svg class="contact__icon" viewBox="0 0 12 12"><rect x="3" y="0" width="6" height="12" rx="1"/></svg>
        0471 625 183
      </li>
      <li class="contact__item">
        <svg class="contact__icon" viewBox="0 0 12 12"><path d="M1,3 C1,1 3,1 6,1 C9,1 11,1 11,3 L9,5 L7,4 L5,4 L3,5 Z M2,7 L10,7 L11,11 L1,11 Z"/></svg>
        1300 872 619
      </li>
      <li class="contact__item">
        <svg class="contact__icon" viewBox="0 0 12 12"><path d="M0,2 L12,2 L12,10 L0,10 Z M1,3 L6,7 L11,3 Z" fill-rule="evenodd"/></svg>
        dean@volkarsystems.com.au
      </li>
      <li class="contact__item">
        <svg class="contact__icon" viewBox="0 0 12 12"><path d="M6,0 C3.5,0 2,2 2,4 C2,7 6,12 6,12 C6,12 10,7 10,4 C10,2 8.5,0 6,0 Z M6,2.5 A1.5,1.5 0 1 0 6,5.5 A1.5,1.5 0 1 0 6,2.5 Z" fill-rule="evenodd"/></svg>
        4/18 Galloway Crest Road, Harwood Vale NSW 2163
      </li>
    </ul>
  </section>

  <section class="card card--back" aria-label="Business card, brand side">
    <svg class="card__swoosh" viewBox="0 0 520 317" preserveAspectRatio="none" aria-hidden="true">
      <path d="M200,317 C300,248 420,220 520,212 L520,317 Z" fill="var(--slate)"/>
      <path d="M168,317 C290,232 420,196 520,186 L520,200 C420,210 300,242 196,317 Z" fill="var(--red)"/>
    </svg>
    <div class="brand"><span class="brand__square"></span>Volkar Systems</div>
    <p class="website">www.volkarsystems.com.au</p>
  </section>

</main>
</body>
</html>
```